Bright Harbor Realty

We need a good looking flyer for our real estate company to impress people who are considering to sell their homes for as low as 1.5% listing commission. Please see flyer examples for reference.
555-318-4906

```html
<!DOCTYPE html>
<html lang="en">
<head>
<meta charset="utf-8">
<title>Bright Harbor Realty – Just Sold Postcard</title>
<link href="https://fonts.googleapis.com/css2?family=Roboto+Condensed:ital,wght@0,400;0,700;1,400;1,700;1,900&family=Oswald:wght@400;500;700&display=swap" rel="stylesheet">
<style>
  :root{
    --page:#e9e9ea;
    --card:#ffffff;
    --blue:#0d47a8;
    --red:#e01a1a;
    --ink:#1d1d1d;
    --rule:#2a2a2a;
    --faint:#f1f1f2;
  }
  *{box-sizing:border-box;margin:0;padding:0}
  html,body{width:1200px;height:1200px;overflow:hidden;background:var(--page)}
  body{position:relative;font-family:"Roboto Condensed",sans-serif;color:var(--ink)}

  .card{position:absolute;top:198px;width:574px;height:805px;background:var(--card);overflow:hidden}
  .card--front{left:24px}
  .card--back{left:614px}

  .front-backdrop{position:absolute;inset:0;background:linear-gradient(180deg,#fafafa 0%,#ececec 45%,#f4f4f4 75%,#ffffff 100%)}

  .brand{position:absolute;display:flex;align-items:center;gap:6px;font-family:"Roboto Condensed",sans-serif;font-weight:700;color:var(--blue);font-size:19px;line-height:1.05}
  .brand__mark{width:14px;height:14px;background:var(--blue);flex:none}
  .card--front .brand{left:22px;top:58px;width:140px}
  .card--back .brand{left:26px;top:58px;width:140px}

  .pitch{position:absolute;font-style:italic;line-height:1.1}
  .pitch__lead{font-size:18px;font-weight:400}
  .pitch__lead strong{color:var(--blue);font-weight:700}
  .pitch__strong{font-size:18px;font-weight:700}
  .pitch__call{font-size:12px;margin-top:2px}
  .pitch__phone{font-size:26px;font-weight:900;color:var(--blue);letter-spacing:.5px;margin-top:-2px}
  .card--front .pitch{right:26px;top:22px;text-align:right}
  .card--back .pitch{left:24px;top:150px}

  .headline{position:absolute;left:0;right:0;top:120px;display:flex;justify-content:center;align-items:center;gap:8px}
  .headline__rule{width:60px;height:2px;background:var(--rule)}
  .headline__text{font-family:"Oswald",sans-serif;font-weight:700;font-style:italic;font-size:42px;color:var(--red);letter-spacing:1px;line-height:1}

  .sale{position:absolute;width:236px;text-align:center}
  .sale__photo{display:block;width:236px;height:166px;border:3px solid var(--blue);border-radius:8px}
  .sale__address{margin-top:7px;font-size:11px;font-weight:700;font-style:italic;line-height:1.25}
  .sale__price{color:var(--red)}
  .sale--1{left:34px;top:173px}
  .sale--2{left:302px;top:173px}
  .sale--3{left:34px;top:377px}
  .sale--4{left:302px;top:377px}
  .sale--5{left:307px;top:579px}

  .know{position:absolute;left:24px;top:577px;width:270px}
  .know__title{font-family:"Oswald",sans-serif;font-size:20px;font-weight:500;color:var(--red);line-height:1.1}
  .know__body{font-size:11px;line-height:1.25;text-align:justify}
  .know__body strong{font-weight:700}
  .know__call{font-size:10.5px;font-weight:700;margin-top:6px}
  .know__phone{font-size:22px;color:var(--blue);font-weight:400;line-height:1.1}

  .agent{position:absolute;left:34px;top:684px;width:124px;height:124px}

  .stamp{position:absolute;left:501px;top:24px;width:49px;height:49px;border:1.5px solid var(--rule)}
  .address-line{position:absolute;left:419px;width:131px;height:1px;background:var(--rule)}
</style>
</head>
<body>

<section class="card card--front" aria-label="Postcard front">
  <div class="front-backdrop" role="img" aria-label="Faint greyscale photo of a home behind the layout"></div>

  <div class="brand"><span class="brand__mark"></span><span>Bright Harbor Realty</span></div>

  <div class="pitch">
    <p class="pitch__lead">List for <strong>1.5% Commission,</strong></p>
    <p class="pitch__strong">Still Receive Top Marketing!</p>
    <p class="pitch__call">Call Us Today and Save Thousands!</p>
    <p class="pitch__phone">(555) 318 - 4906</p>
  </div>

  <div class="headline">
    <span class="headline__rule"></span>
    <h1 class="headline__text">JUST SOLD</h1>
    <span class="headline__rule"></span>
  </div>

  <figure class="sale sale--1">
    <div class="sale__photo" role="img" aria-label="Photo of a green single-storey house with garage and driveway" style="background:linear-gradient(180deg,#a9c7e6 0%,#7d9a4a 45%,#b3b3a8 70%,#5f9a3a 100%)"></div>
    <figcaption class="sale__address">11713 Willow Bend Circle<br>Cedar Springs, FL 33001 - <span class="sale__price">$250,000</span></figcaption>
  </figure>

  <figure class="sale sale--2">
    <div class="sale__photo" role="img" aria-label="Photo of a grey stone single-storey house with lawn" style="background:linear-gradient(180deg,#6f9fd6 0%,#b9cfe6 35%,#8c8c8c 55%,#5d9a34 75%,#4c8a2a 100%)"></div>
    <figcaption class="sale__address">16311 E Meadowlark Drive<br>Palm Hollow, FL 33002 - <span class="sale__price">$280,000</span></figcaption>
  </figure>

  <figure class="sale sale--3">
    <div class="sale__photo" role="img" aria-label="Photo of a light blue house with palm trees and driveway" style="background:linear-gradient(180deg,#3f86d6 0%,#9cc4ea 35%,#bcd6e4 50%,#5c9a34 70%,#c9b79c 100%)"></div>
    <figcaption class="sale__address">13972 Bayberry Circle<br>Cedar Springs, FL 33001 - <span class="sale__price">$335,000</span></figcaption>
  </figure>

  <figure class="sale sale--4">
    <div class="sale__photo" role="img" aria-label="Photo of two-storey tan townhouses with parked cars" style="background:linear-gradient(180deg,#8fb3dc 0%,#d8e3ee 25%,#b79b85 50%,#9a8a7a 70%,#c8c8c8 100%)"></div>
    <figcaption class="sale__address">2062 Lantern Circle E<br>Seabrook Beach, FL 33003 - <span class="sale__price">$229,500</span></figcaption>
  </figure>

  <figure class="sale sale--5">
    <div class="sale__photo" role="img" aria-label="Photo of two-storey tan townhouses with parked cars" style="background:linear-gradient(180deg,#8fb3dc 0%,#d8e3ee 25%,#b79b85 50%,#9a8a7a 70%,#c8c8c8 100%)"></div>
    <figcaption class="sale__address">5135 Fairway Oaks Drive<br>Coral Ridge, FL 33004 - <span class="sale__price">$550,000</span></figcaption>
  </figure>

  <div class="know">
    <h2 class="know__title">Did You Know?</h2>
    <p class="know__body">On average, our customers save <strong>$8,750</strong> when they choose us... and they still receive top marketing, service and representation!</p>
    <p class="know__call">Call Us Today and Save Thousands!</p>
    <p class="know__phone">(555) 318 -4906</p>
  </div>

  <svg class="agent" viewBox="0 0 124 124" role="img" aria-label="Portrait photo of the agent in a dark suit">
    <circle cx="62" cy="62" r="60" fill="#c9c9c9"/>
    <path d="M6 44 A60 60 0 0 1 118 44" fill="none" stroke="var(--blue)" stroke-width="3"/>
  </svg>
</section>

<section class="card card--back" aria-label="Postcard back">
  <div class="brand"><span class="brand__mark"></span><span>Bright Harbor Realty</span></div>

  <div class="pitch">
    <p class="pitch__lead">List for <strong>1.5% Commission,</strong></p>
    <p class="pitch__strong">Still Receive Top Marketing!</p>
    <p class="pitch__call">Call Us Today and Save Thousands!</p>
    <p class="pitch__phone">(555) 318 - 4906</p>
  </div>

  <div class="stamp" aria-label="Stamp area"></div>
  <div class="address-line" style="top:112px"></div>
  <div class="address-line" style="top:133px"></div>
  <div class="address-line" style="top:154px"></div>
</section>

</body>
</html>
```